Acrylic print memorial plaque for entrance

I need a design for an acrylic print in DIN A0 portrait format or 1.5x DIN A0.

The top 40% should contain the lettering "Veronika's Meadow Haven." The lettering should frame three pictures. In the center is a portrait of Vero (Veronika), with "In Memoriam" below the name and the dates *November 20, 1980 †May 15, 2024. The head of the horse Solvina should be placed on the left, and Bellis's head on the right.
The next 35% of the area should depict the portraits of Gerhard (left), Henrik (middle), and Frieda (right) in the upper part. Each with their name underneath. The lower part of this 35% should contain

“Our helpers:”
Then the portraits of Dieter, Helene, Uschi & Glenn should be taken in the following order. Each one should also have its name underneath the portrait.
The remaining 25% should contain the following:
“We would like to thank:
Klaus & Ingrid for their valuable support, and Hanni for her help and tips on handling the horse. We would also like to thank the Weibel family, especially Beni & Sabine and Flori & Greta, for allowing us to create this paradise according to our ideas and for the construction. And, of course, the many other helpers and supporters.
The images should be isolated as much as possible and scaled to fit the print size. If possible, only the faces (head + neck) should be included.

Cut out, shape, or mirror the horse heads depending on the design.

The various images can be used as backgrounds, provided the design allows it.

Target Market(s)

No target mark, memorial plaque for the stable

Font styles to use
Serif
Decorative
Script

Requirements
Must have
• Honest, Authentic, Devotional
Should not have
• Kitsch, too playful.

```html
<!DOCTYPE html>
<html lang="en">
<head>
<meta charset="utf-8">
<title>Veronika's Meadow Haven – In Memoriam</title>
<link href="https://fonts.googleapis.com/css2?family=Rye&family=Bree+Serif&family=Crimson+Text&display=swap" rel="stylesheet">
<style>
  :root{
    --brown:#5a3f30;
    --brown-dark:#4a3226;
    --cream:#f6ead8;
    --paper-top:#efdfc9;
    --paper-mid:#e9cfae;
    --paper-low:#e4ccb0;
    --ink:#5b4234;
    --text:#6a4e3f;
  }
  *{box-sizing:border-box;margin:0;padding:0}
  html,body{width:848px;height:1200px;overflow:hidden;background:var(--cream)}
  .plaque{position:relative;width:848px;height:1200px;overflow:hidden;
    background:linear-gradient(180deg,var(--paper-top) 0%,#f1d9bb 35%,var(--paper-mid) 55%,var(--paper-low) 80%,#ead6bf 100%);}
  .frame-outer{position:absolute;left:18px;top:18px;width:812px;height:1162px;border:4px solid var(--brown);border-radius:40px}
  .frame-inner{position:absolute;left:30px;top:30px;width:788px;height:1138px;border:2px solid var(--brown)}
  .corner{position:absolute;width:86px;height:86px;border-radius:50%;background:var(--brown)}
  .corner.tl{left:-43px;top:-43px}.corner.tr{right:-43px;top:-43px}
  .corner.bl{left:-43px;bottom:-43px}.corner.br{right:-43px;bottom:-43px}

  .title-band{position:absolute;left:30px;top:30px;width:788px;height:66px;background:var(--brown);
    display:flex;align-items:center;justify-content:center}
  .title-band h1{font-family:"Rye",serif;font-weight:400;color:var(--cream);font-size:38px;letter-spacing:1px}

  .photo{position:absolute;border:5px solid var(--brown);border-radius:50%}
  .photo.horse-left{left:66px;top:137px;width:242px;height:252px;background:linear-gradient(135deg,#c9c4bf,#5a5350 55%,#2c2726)}
  .photo.horse-right{left:540px;top:137px;width:242px;height:252px;background:linear-gradient(135deg,#8a8a80,#a5532c 50%,#6c3a22)}
  .photo.portrait{left:292px;top:105px;width:263px;height:265px;background:linear-gradient(160deg,#dad7d2,#caa088 50%,#3b2a24)}

  .memorial{position:absolute;left:258px;top:368px;width:331px;height:56px;background:var(--brown);
    clip-path:polygon(14px 0,317px 0,331px 14px,331px 42px,317px 56px,14px 56px,0 42px,0 14px);
    display:flex;align-items:center;justify-content:center}
  .memorial::before{content:"";position:absolute;inset:5px;border:1.5px solid var(--cream);
    clip-path:polygon(10px 0,calc(100% - 10px) 0,100% 10px,100% calc(100% - 10px),calc(100% - 10px) 100%,10px 100%,0 calc(100% - 10px),0 10px)}
  .memorial h2{font-family:"Bree Serif",serif;font-weight:400;color:var(--cream);font-size:34px;margin-top:-4px}
  .name-pill{position:absolute;left:302px;top:421px;width:242px;height:31px;background:#fff;border:2px solid var(--brown);
    border-radius:16px;text-align:center;font-family:"Rye",serif;color:var(--brown);font-size:18px;line-height:27px}
  .dates{position:absolute;left:0;top:455px;width:848px;text-align:center;font-family:"Crimson Text",serif;color:var(--ink);font-size:20px}

  .family{position:absolute;top:506px;width:184px;height:153px;border:4px solid var(--brown)}
  .family.gerhard{left:90px;background:linear-gradient(160deg,#6c7470,#c8b8aa 50%,#8a8178)}
  .family.henrik{left:332px;background:linear-gradient(160deg,#5a4a40,#c59a80 50%,#3a2f2a)}
  .family.frieda{left:574px;background:linear-gradient(160deg,#4f7a90,#c99a84 50%,#e0dcd8)}
  .tag{position:absolute;left:50%;transform:translateX(-50%);background:var(--brown);color:var(--cream);
    font-family:"Bree Serif",serif;text-align:center;border:1.5px solid var(--cream);outline:2px solid var(--brown)}
  .family .tag{bottom:-13px;width:128px;height:27px;font-size:18px;line-height:24px;border-radius:4px;letter-spacing:.5px}

  .helpers{position:absolute;left:91px;top:715px;width:666px;height:164px;border:3px solid var(--brown)}
  .helpers-label{position:absolute;left:348px;top:702px;width:150px;height:28px;background:var(--brown);color:var(--cream);
    font-family:"Bree Serif",serif;font-size:17px;line-height:27px;text-align:center;
    clip-path:polygon(6px 0,144px 0,150px 6px,150px 22px,144px 28px,6px 28px,0 22px,0 6px)}
  .helper{position:absolute;top:734px;width:150px;height:127px;border:3px solid var(--brown);
    background:linear-gradient(180deg,#3d8fd0 0%,#7dbb6a 38%,#c89a80 55%,#d8c7a8 100%)}
  .helper.dieter{left:110px}.helper.helene{left:270px}.helper.uschi{left:429px}.helper.glenn{left:589px}
  .helper .tag{bottom:-11px;width:112px;height:19px;font-size:12px;line-height:16px;border-radius:10px}

  .thanks-label{position:absolute;left:272px;top:926px;width:303px;height:30px;background:var(--brown);color:var(--cream);
    font-family:"Bree Serif",serif;font-size:19px;line-height:29px;text-align:center;
    clip-path:polygon(6px 0,297px 0,303px 6px,303px 24px,297px 30px,6px 30px,0 24px,0 6px)}
  .thanks{position:absolute;left:78px;top:972px;width:692px;text-align:center;font-family:"Bree Serif",serif;
    color:var(--text);font-size:19px;line-height:28.5px}
</style>
</head>
<body>
<main class="plaque">
  <div class="frame-outer"></div>
  <div class="frame-inner"></div>
  <div class="corner tl"></div><div class="corner tr"></div>
  <div class="corner bl"></div><div class="corner br"></div>

  <header class="title-band"><h1>VERONIKA’S MEADOW HAVEN</h1></header>

  <div class="photo horse-left" role="img" aria-label="Head of the dark horse Solvina in profile"></div>
  <div class="photo horse-right" role="img" aria-label="Head of the chestnut horse Bellis with halter"></div>
  <div class="photo portrait" role="img" aria-label="Portrait of Veronika smiling"></div>

  <div class="memorial"><h2>In Memorial</h2></div>
  <div class="name-pill">VERO (VERONIKA)</div>
  <p class="dates">November 20, 1980 - † May 15, 2024</p>

  <div class="family gerhard" role="img" aria-label="Portrait of Gerhard"><span class="tag">GERHARD</span></div>
  <div class="family henrik" role="img" aria-label="Portrait of Henrik"><span class="tag">HENRIK</span></div>
  <div class="family frieda" role="img" aria-label="Portrait of Frieda"><span class="tag">FRIEDA</span></div>

  <div class="helpers"></div>
  <div class="helpers-label">Our Helpers</div>
  <div class="helper dieter" role="img" aria-label="Portrait of Dieter at the stable"><span class="tag">Dieter</span></div>
  <div class="helper helene" role="img" aria-label="Portrait of Helene at the stable"><span class="tag">Helene</span></div>
  <div class="helper uschi" role="img" aria-label="Portrait of Uschi at the stable"><span class="tag">Uschi</span></div>
  <div class="helper glenn" role="img" aria-label="Portrait of Glenn outdoors"><span class="tag">Glenn</span></div>

  <div class="thanks-label">We would like to thanks:</div>
  <p class="thanks">Klaus &amp; Ingrid for their valuable support and Hanni for her help and tips on handling the horse. We would also like to thank the Weibel Family, especially Beni &amp; Sabine also Flori &amp; Greta, for allowing us to create this paradise according to our ideas and for the construction.<br>And of course, the many other helpers and supportes.</p>
</main>
</body>
</html>
```